EG 1 page flyer

I need a flyer design for a financial risk advisory business. I like the layout of the example on your site, for Corbin Delph (attached). Our business needs to show strength, safety, knowledge and security. We provide financial advice.

I have uploaded the front page of our larger brochure. I would like the man with the umbrella with the caption and the logo / brand on the front page, but with portrait orientation, instead of landscape.

For the second page (the back), I have got some ideas of the kinds of things I would want written on the attached Power Point. But it needs to be arranged better, with perhaps the Elsie's Gate Logo on there as well, to break up all the writing. Attached is an example of how it might look, but I want different formatting and layout ideas, that look better, more professional etc.

The page 1 comment what is elsies gate? predicting ......... would look better all the way along the bottom of the page, but i couldn't get the formatting right.

Financial

```html
<!DOCTYPE html>
<html lang="en">
<head>
<meta charset="utf-8">
<title>Elsie's Gate – Flyer</title>
<link rel="stylesheet" href="https://fonts.googleapis.com/css2?family=PT+Sans:wght@400;700&display=swap">
<style>
  :root{
    --stage:#000000;
    --sky:#5dbde7;
    --sky-light:#bfe6f8;
    --paper:#ffffff;
    --navy:#2b2f6e;
    --teal:#1d7db2;
    --drop-pale:#dfeef5;
    --suit:#161616;
    --suit-soft:#2e2e2e;
  }
  *{box-sizing:border-box;margin:0;padding:0}
  html,body{width:1200px;height:896px;overflow:hidden;background:var(--stage);font-family:"PT Sans",Arial,sans-serif}
  .canvas{position:relative;width:1200px;height:896px}
  .page{position:absolute;top:20px;width:568px;height:852px;background:var(--paper);overflow:hidden}
  .page--front{left:19px}
  .page--back{left:612px}

  .band{position:absolute;top:0;height:100%}
  .front-band{left:0;width:272px;background:radial-gradient(circle at 90px 70px,var(--sky-light) 0,var(--sky) 190px,var(--sky) 100%)}
  .back-band{left:0;width:283px;background:var(--sky)}

  .rain{position:absolute;top:0;height:100%}
  .front-rain{left:272px;width:296px;background:linear-gradient(180deg,var(--drop-pale),var(--paper) 45%,var(--drop-pale))}
  .back-rain{left:0;width:283px;background:linear-gradient(180deg,#8ed0ee,var(--sky) 40%,var(--sky))}

  .figure{position:absolute;top:195px;width:223px;height:582px;border-radius:6px;
    background:linear-gradient(180deg,var(--suit-soft) 0,var(--suit) 30%,var(--suit) 100%)}
  .front-figure{left:293px}
  .back-figure{left:13px}

  .brand{position:absolute;color:var(--navy)}
  .brand-name{display:block;font-size:46px;font-weight:700;line-height:1;letter-spacing:-0.5px;white-space:nowrap}
  .brand-tag{display:block;font-size:12px;color:var(--teal);margin-top:4px;white-space:nowrap}
  .brand-dot{position:absolute;width:46px;height:46px;border-radius:50%;background:var(--navy)}
  .front-brand{left:22px;top:118px}
  .front-brand .brand-dot{left:176px;top:-66px}
  .back-brand{left:320px;top:404px}
  .back-brand .brand-dot{left:176px;top:-62px}

  .rule{position:absolute;text-align:center;font-weight:700}
  .rule-q{color:var(--teal)}
  .rule-quote{color:var(--navy)}
  .front-rule{left:0;width:272px;top:604px}
  .front-rule .rule-q{font-size:21px;line-height:24px}
  .front-rule .rule-quote{font-size:23px;line-height:25px;margin-top:30px}

  .forecast{position:absolute;left:283px;width:285px;top:113px;text-align:center;color:var(--navy);font-size:24px;line-height:30px}

  .services{position:absolute;left:283px;width:285px;top:522px;text-align:center;color:var(--navy)}
  .services-title{font-size:22px;font-weight:700;line-height:28px}
  .services-list{list-style:none;margin-top:20px;font-size:20px}
  .services-list li{height:42px}
  .services-list li::before{content:"• "}

  .back-rule{left:283px;width:285px;top:776px}
  .back-rule .rule-q{font-size:12px}
  .back-rule .rule-quote{font-size:12px;font-weight:400;margin-top:2px;line-height:16px}
</style>
</head>
<body>
<main class="canvas">
  <section class="page page--front">
    <div class="band front-band"></div>
    <div class="rain front-rain" role="img" aria-label="Falling raindrop pattern in light blue and grey"></div>
    <div class="figure front-figure" role="img" aria-label="Photo of a man in a dark suit and bowler hat seen from behind, holding a black umbrella"></div>
    <div class="brand front-brand">
      <span class="brand-dot"></span>
      <span class="brand-name">Elsie's Gate</span>
      <span class="brand-tag">Steady advice &nbsp;Firm ground</span>
    </div>
    <div class="rule front-rule">
      <p class="rule-q">What is<br>Elsie's Gate?</p>
      <p class="rule-quote">“Predicting rain<br>doesn’t count;<br>building<br>arks does”.</p>
    </div>
  </section>

  <section class="page page--back">
    <div class="band back-band"></div>
    <div class="rain back-rain" role="img" aria-label="Falling raindrop pattern in white and pale blue"></div>
    <div class="figure back-figure" role="img" aria-label="Photo of a man in a dark suit and bowler hat seen from behind, holding a black umbrella"></div>
    <p class="forecast">Whatever the<br>Financial<br>Forecast…<br>It pays to<br>be prepared!</p>
    <div class="brand back-brand">
      <span class="brand-dot"></span>
      <span class="brand-name">Elsie's Gate</span>
      <span class="brand-tag">Steady advice &nbsp;Firm ground</span>
    </div>
    <div class="services">
      <h2 class="services-title">Financial Risk<br>Advisory:</h2>
      <ul class="services-list">
        <li>DEBT &amp; FUNDING</li>
        <li>MARKET RISK</li>
        <li>ACTIVE ENGAGEMENT</li>
      </ul>
    </div>
    <div class="rule back-rule">
      <p class="rule-q">What is Elsie's Gate?</p>
      <p class="rule-quote">“Predicting rain doesn’t count;<br>building arks does”.</p>
    </div>
  </section>
</main>
</body>
</html>
```